Health care technology software systems

We have a solid logo. We have company colors that will need to be used as well. We just need a great business card design. We sell to health plans but want to be modern
Updates

Need extra days to review

Target Market(s)

Health technology sector selling into Health Plans

Industry/Entity Type

Health Care Technology

Contact Information for Business Card

Name, title, address, phone number, email

Requirements
Must have
• Use of Kembrata corporate colors - Uploaded w/ our logos

```html
<!DOCTYPE html>
<html lang="en">
<head>
<meta charset="utf-8">
<title>Kembrata — Business Card</title>
<link rel="stylesheet" href="https://fonts.googleapis.com/css2?family=Inter:wght@300;400;600&display=swap">
<style>
  :root {
    --page-bg: #dcdcdc;
    --card-bg: #f3f5f6;
    --panel-dark: #1d1f21;
    --ink: #333638;
    --brand-blue: #2f7fc0;
    --brand-green: #5aa22c;
    --disc-light: #e6eaec;
    --disc-edge: #c9cfd2;
  }
  * { box-sizing: border-box; margin: 0; padding: 0; }
  html, body {
    width: 1200px; height: 969px; overflow: hidden;
    background: var(--page-bg);
    font-family: "Inter", Arial, sans-serif;
    color: var(--ink);
  }
  .card {
    position: absolute; left: 75px; top: 185px;
    width: 1050px; height: 600px;
    border-radius: 34px; overflow: hidden;
    background: var(--card-bg);
    box-shadow: 0 2px 10px rgba(0,0,0,0.18);
  }
  .card__panel {
    position: absolute; right: 0; top: 0;
    width: 270px; height: 100%;
    background: var(--panel-dark);
  }
  .card__disc {
    position: absolute; left: 455px; top: 10px;
    width: 595px; height: 595px; border-radius: 50%;
    background: radial-gradient(circle at 45% 45%, #f7f9fa 0%, var(--disc-light) 70%, var(--disc-edge) 100%);
  }
  .card__info { position: absolute; left: 66px; top: 100px; }
  .wordmark {
    font-weight: 300; font-size: 82px; letter-spacing: 1px;
    line-height: 1; color: var(--ink);
  }
  .person__name {
    margin-top: 42px;
    font-weight: 600; font-size: 35px; color: var(--brand-blue);
  }
  .person__title {
    margin-top: 2px;
    font-size: 24px; color: var(--brand-green);
  }
  .address {
    margin-top: 26px;
    font-size: 24px; line-height: 31px; font-style: normal;
  }
  .contacts { margin-top: 24px; list-style: none; }
  .contacts li {
    display: flex; align-items: center; gap: 14px;
    font-size: 24px; line-height: 31px;
  }
  .contacts svg { width: 20px; height: 20px; fill: var(--brand-green); flex: none; }
</style>
</head>
<body>
  <div class="card">
    <div class="card__panel"></div>
    <div class="card__disc"></div>

    <div class="card__info">
      <div class="wordmark">kembrata</div>
      <div class="person__name">Daniel Harper</div>
      <div class="person__title">President</div>
      <address class="address">4213 Alder Creek Road<br>Anchorage, Alaska 99507</address>
      <ul class="contacts">
        <li>
          <svg viewBox="0 0 24 24" aria-hidden="true"><path d="M6.6 10.8a15.5 15.5 0 0 0 6.6 6.6l2.2-2.2a1 1 0 0 1 1-.25 11.4 11.4 0 0 0 3.6.57 1 1 0 0 1 1 1V20a1 1 0 0 1-1 1A17 17 0 0 1 3 4a1 1 0 0 1 1-1h3.5a1 1 0 0 1 1 1c0 1.25.2 2.45.57 3.6a1 1 0 0 1-.25 1z"/></svg>
          555-214-7730
        </li>
        <li>
          <svg viewBox="0 0 24 24" aria-hidden="true"><path d="M7 1h10a2 2 0 0 1 2 2v18a2 2 0 0 1-2 2H7a2 2 0 0 1-2-2V3a2 2 0 0 1 2-2zm0 3v14h10V4zm5 15.5a1 1 0 1 0 0 2 1 1 0 0 0 0-2z"/></svg>
          555-308-4162
        </li>
        <li>
          <svg viewBox="0 0 24 24" aria-hidden="true"><path d="M2 5h20v14H2zm2 2v.5l8 5 8-5V7zm0 2.8V17h16V9.8l-8 5z"/></svg>
          dharper@kembrata.com
        </li>
        <li>
          <svg viewBox="0 0 24 24" aria-hidden="true"><circle cx="12" cy="12" r="10"/></svg>
          www.kembrata.com
        </li>
      </ul>
    </div>
  </div>
</body>
</html>
```